Book cover

I am working with my publisher to publish my book They came up with a book cover but I don't like it. I want to see different designs. The book Title is Shiftcraftery the subtitle How to Steer Upheaval with Focus, Poise & Resolve by Marilyn T. Hargreave
I want to use my Brand Colors including the blue. I am uploading the covers of my other book. This is a professional leadership book. The publisher will make the cover when providing them a new design. the Shiftcraftery one is one I played with on Canva. I would like more color and to incorporate the blue. I want a spot at the top where I can write a quote. Shiftcraftery is one word in the text so should be the same on the cover. I want the cover to show energy movement and am open to an image too. I am attaching logos for the feel of the brand and brand rgb codes.

```html
<!DOCTYPE html>
<html lang="en">
<head>
<meta charset="UTF-8">
<title>Shiftcraftery – Book Cover</title>
<link href="https://fonts.googleapis.com/css2?family=Cinzel:wght@400;500&family=Playfair+Display:wght@400&family=Quicksand:wght@500&display=swap" rel="stylesheet">
<style>
  :root {
    --teal: #0896a4;
    --red: #d92633;
    --red-soft: #e8545e;
    --white: #ffffff;
    --ink: #111111;
    --stage: #6b6b6b;
    --photo-dark: #0b0b0b;
    --photo-mid: #262626;
    --photo-light: rgba(200, 200, 200, 0.22);
    --photo-red: rgba(217, 38, 51, 0.55);
  }
  * { margin: 0; padding: 0; box-sizing: border-box; }
  html, body {
    width: 1200px;
    height: 847px;
    overflow: hidden;
    background: var(--stage);
  }
  .canvas {
    width: 1200px;
    height: 847px;
    display: flex;
    align-items: center;
    justify-content: center;
  }
  .cover {
    width: 534px;
    height: 800px;
    display: flex;
    flex-direction: column;
    box-shadow: 0 6px 24px rgba(0,0,0,0.35);
  }
  .band-teal { height: 19.5px; background: var(--teal); flex: none; }
  .quote-band {
    height: 108px;
    background: var(--red);
    flex: none;
    display: flex;
    align-items: center;
    justify-content: center;
  }
  .quote {
    font-family: "Quicksand", sans-serif;
    font-weight: 500;
    color: var(--white);
    font-size: 19px;
    line-height: 19px;
    text-align: center;
    letter-spacing: 0.3px;
    word-spacing: 3px;
    position: relative;
    margin-top: -6px;
  }
  .quote-mark {
    position: absolute;
    font-family: "Playfair Display", serif;
    color: var(--red-soft);
    font-size: 58px;
    line-height: 1;
  }
  .quote-mark.open { left: -20px; top: -12px; }
  .quote-mark.close { right: 12px; bottom: -34px; }
  .title-band {
    height: 199px;
    background: var(--white);
    flex: none;
    display: flex;
    align-items: center;
    justify-content: center;
  }
  .title {
    font-family: "Playfair Display", serif;
    fill: var(--red);
  }
  .photo {
    height: 271px;
    flex: none;
    background:
      radial-gradient(ellipse 14% 18% at 37% 36%, var(--photo-red) 0%, rgba(217,38,51,0) 100%),
      radial-gradient(ellipse 38% 55% at 84% 45%, var(--photo-light) 0%, rgba(200,200,200,0) 100%),
      radial-gradient(ellipse 45% 30% at 78% 88%, var(--photo-light) 0%, rgba(200,200,200,0) 100%),
      linear-gradient(100deg, var(--photo-dark) 0%, var(--photo-mid) 55%, var(--photo-dark) 100%);
  }
  .subtitle-band {
    height: 106px;
    background: var(--white);
    flex: none;
    display: flex;
    align-items: center;
    justify-content: center;
  }
  .subtitle {
    font-family: "Cinzel", serif;
    font-weight: 500;
    color: var(--ink);
    font-size: 27px;
    line-height: 24px;
    text-align: center;
    text-transform: uppercase;
  }
  .author-band {
    height: 76px;
    background: var(--red);
    flex: none;
    display: flex;
    align-items: center;
    justify-content: center;
  }
  .author {
    font-family: "Cinzel", serif;
    font-weight: 400;
    color: var(--white);
    font-size: 36px;
    text-transform: uppercase;
    letter-spacing: 0.5px;
  }
</style>
</head>
<body>
<main class="canvas">
  <article class="cover">
    <div class="band-teal"></div>
    <header class="quote-band">
      <p class="quote">
        <span class="quote-mark open">“</span>Shiftcraftery is the essential playbook to<br>turn uncertainity into possiblity<span class="quote-mark close">”</span>
      </p>
    </header>
    <section class="title-band">
      <svg width="480" height="120" viewBox="0 0 480 120">
        <text class="title" x="240" y="96" font-size="104" text-anchor="middle" textLength="470" lengthAdjust="spacingAndGlyphs">SHIFTCRAFTERY</text>
      </svg>
    </section>
    <div class="photo" role="img" aria-label="Photo of white paper boats sailing in diagonal rows across a dark chalkboard, with one red paper boat breaking away in its own direction"></div>
    <section class="subtitle-band">
      <p class="subtitle">How to Steer Upheaval<br>with Focus,<br>Poise &amp; Resolve</p>
    </section>
    <footer class="author-band">
      <p class="author">Marilyn T. Hargreave</p>
    </footer>
    <div class="band-teal"></div>
  </article>
</main>
</body>
</html>
```